I'm a magician . hypnotist also a good barber. I need this all to be shown in good detail on the cards.

Magician

Magician/ hypnotist/barber Morris quill. One of the best. Tel 07412 638204
Email.Velvetowl27@postmail-example.net
Title of card velvet owl.

```html
<!DOCTYPE html>
<html lang="en">
<head>
<meta charset="utf-8">
<title>Velvet Owl – Business Card</title>
<link rel="stylesheet" href="https://fonts.googleapis.com/css2?family=Metamorphous&family=Open+Sans:ital,wght@0,400;1,400&family=Parisienne&family=Lobster+Two:ital,wght@1,700&display=swap">
<style>
  :root {
    --page-bg: #f2f2f2;
    --card-bg: #08050c;
    --violet-deep: #2a1a6e;
    --violet: #4a3aa8;
    --smoke-blue: #6fa8e0;
    --smoke-pink: #c83c8c;
    --title-green: #dbe98a;
    --title-glow: #8fb834;
    --subtitle-blue: #8fd0ee;
    --flame: #e8682a;
    --silver: #e4e4e8;
    --silver-dark: #9a9aa4;
    --tagline-tan: #c9a878;
    --email-grey: #d6d6de;
  }
  * { margin: 0; padding: 0; box-sizing: border-box; }
  html, body {
    width: 1200px; height: 1200px; overflow: hidden;
    background: var(--page-bg);
  }
  .business-card {
    position: absolute;
    left: 50px; top: 237px;
    width: 1100px; height: 725px;
    overflow: hidden;
    background:
      radial-gradient(ellipse 260px 170px at 640px 600px, rgba(200,60,140,0.55), transparent 70%),
      radial-gradient(ellipse 420px 300px at 560px 420px, rgba(70,110,200,0.28), transparent 75%),
      var(--card-bg);
  }
  .performer-art {
    position: absolute; left: 0; top: 0;
    width: 560px; height: 725px;
    background:
      radial-gradient(ellipse 260px 340px at 150px 380px, rgba(111,168,224,0.55), transparent 70%),
      linear-gradient(90deg, var(--violet-deep) 0%, var(--violet) 35%, rgba(42,26,110,0.5) 70%, transparent 100%);
  }
  .card-text {
    position: absolute; left: 390px; right: 0; top: 0; bottom: 0;
    text-align: center;
  }
  .card-text > * { position: absolute; left: 0; right: 0; white-space: nowrap; }
  .brand-title {
    top: 68px;
    font-family: "Metamorphous", serif;
    font-size: 82px; letter-spacing: 2px;
    color: var(--title-green);
    text-shadow: 0 0 10px var(--title-glow);
    text-transform: uppercase;
  }
  .services {
    top: 200px;
    font-family: "Open Sans", sans-serif; font-style: italic;
    font-size: 38px; color: var(--subtitle-blue);
  }
  .services .divider {
    display: inline-block; width: 12px; height: 16px;
    border-radius: 50% 50% 50% 50% / 60% 60% 40% 40%;
    background: var(--flame); margin: 0 6px; vertical-align: 2px;
  }
  .performer-name {
    top: 300px;
    font-family: "Metamorphous", serif;
    font-size: 66px; font-variant: small-caps;
    color: var(--silver);
    text-shadow: 0 2px 0 var(--silver-dark);
  }
  .tagline {
    top: 392px;
    font-family: "Parisienne", cursive;
    font-size: 44px; color: var(--tagline-tan);
  }
  .phone {
    top: 510px;
    font-family: "Lobster Two", cursive; font-style: italic; font-weight: 700;
    font-size: 56px; color: var(--silver);
  }
  .email {
    top: 628px;
    font-family: "Open Sans", sans-serif;
    font-size: 34px; color: var(--email-grey);
  }
</style>
</head>
<body>
  <section class="business-card">
    <div class="performer-art" role="img" aria-label="Magician in top hat and white gloves with flying playing cards, scissors and swirling blue smoke"></div>
    <div class="card-text">
      <h1 class="brand-title">Velvet Owl</h1>
      <p class="services">Magician<span class="divider"></span>Hypnotist<span class="divider"></span>Barber</p>
      <h2 class="performer-name">Morris Quill</h2>
      <p class="tagline">One of the best!</p>
      <p class="phone">Tel.: 07412 638204</p>
      <p class="email">e-mail: velvetowl27@postmail-example.net</p>
    </div>
  </section>
</body>
</html>
```